Tarvimoor business cards

Need fresh design for our business cards. Logo must be specific, we are open for everything else.

Contact Information for Business Card

phrase "GMP & JANITORIAL SERVICES" should be used as main point of card

Colors
3176b5
3276b5
85acd3
cedeed
ffffff
0292cd
33a6d7
85cae6
cee9f5

Requirements
Must have
• The logo
Should not have
• crowded designs

```html
<!DOCTYPE html>
<html lang="en">
<head>
<meta charset="utf-8">
<title>Tarvimoor business cards</title>
<link rel="stylesheet" href="https://fonts.googleapis.com/css2?family=Open+Sans:wght@400;600&display=swap">
<style>
  :root {
    --brand-blue: #3176b5;
    --brand-cyan: #0292cd;
    --line-blue: #85acd3;
    --text-grey: #4a4a4a;
    --paper-front: #f1f1f0;
    --paper-back: #ffffff;
    --stage: #e4e6e8;
  }
  * { box-sizing: border-box; margin: 0; padding: 0; }
  html, body {
    width: 1200px; height: 1200px; overflow: hidden;
    background: var(--stage);
    font-family: "Open Sans", sans-serif;
  }
  .sheet {
    width: 1200px; height: 1200px;
    display: flex; flex-direction: column; align-items: center; justify-content: center;
    gap: 70px;
  }
  .card {
    width: 700px; height: 400px;
    box-shadow: 0 6px 18px rgba(0,0,0,0.12);
    position: relative;
  }
  .card--front {
    background: var(--paper-front);
    display: flex; align-items: center; justify-content: center;
  }
  .card--back {
    background: var(--paper-back);
    display: flex; align-items: center;
  }
  .lockup {
    display: flex; flex-direction: column; align-items: flex-end;
  }
  .wordmark {
    display: flex; align-items: center; gap: 14px;
    color: var(--brand-blue);
    font-weight: 400;
    letter-spacing: 0.16em;
    text-transform: uppercase;
    line-height: 1;
  }
  .wordmark__dot {
    width: 14px; height: 14px; border-radius: 50%;
    background: var(--brand-blue);
  }
  .tagline {
    color: var(--brand-blue);
    font-weight: 400;
    text-transform: uppercase;
    letter-spacing: 0.22em;
    white-space: nowrap;
  }
  .card--front .wordmark { font-size: 56px; }
  .card--front .tagline { font-size: 14px; margin-top: 12px; }
  .card--back .wordmark { font-size: 34px; }
  .card--back .wordmark__dot { width: 10px; height: 10px; }
  .card--back .tagline { font-size: 10px; margin-top: 8px; letter-spacing: 0.2em; }
  .back__brand {
    width: 390px; display: flex; justify-content: center;
    padding-left: 20px; margin-top: 70px;
  }
  .back__divider {
    width: 1px; height: 170px; background: var(--line-blue);
    margin-top: -10px;
  }
  .contact {
    padding-left: 34px; margin-top: -60px;
    color: var(--text-grey);
  }
  .contact__name {
    color: var(--brand-blue); font-weight: 600; font-size: 26px; line-height: 1.1;
  }
  .contact__role { font-size: 15px; margin-bottom: 12px; }
  .contact__list { list-style: none; font-size: 15px; line-height: 1.55; }
  .contact__item { display: flex; align-items: flex-start; gap: 10px; }
  .contact__item svg { width: 14px; height: 14px; margin-top: 5px; fill: var(--brand-blue); flex: none; }
  .contact__item--address { margin-bottom: 8px; }
</style>
</head>
<body>
<main class="sheet">
  <section class="card card--front" aria-label="Card front">
    <div class="lockup">
      <div class="wordmark"><span class="wordmark__dot"></span>Tarvimoor</div>
      <p class="tagline">GMP &amp; Janitorial Services</p>
    </div>
  </section>

  <section class="card card--back" aria-label="Card back">
    <div class="back__brand">
      <div class="lockup">
        <div class="wordmark"><span class="wordmark__dot"></span>Tarvimoor</div>
        <p class="tagline">GMP &amp; Janitorial Services</p>
      </div>
    </div>
    <div class="back__divider"></div>
    <div class="contact">
      <p class="contact__name">Elias Brandt</p>
      <p class="contact__role">Creative Designer</p>
      <ul class="contact__list">
        <li class="contact__item contact__item--address">
          <svg viewBox="0 0 14 14"><path d="M7 0a5 5 0 0 0-5 5c0 3.6 5 9 5 9s5-5.4 5-9a5 5 0 0 0-5-5zm0 7a2 2 0 1 1 0-4 2 2 0 0 1 0 4z"/></svg>
          <span>Dummy city<br>Dummy Country Land</span>
        </li>
        <li class="contact__item">
          <svg viewBox="0 0 14 14"><path d="M1 4c0-2 12-2 12 0v1.5H10V4H4v1.5H1zM3 6h8l2 6H1z"/></svg>
          <span>1-234-567890</span>
        </li>
        <li class="contact__item">
          <svg viewBox="0 0 14 14"><path d="M0 3h14v1L7 8 0 4zm0 2.5L7 9.5l7-4V12H0z"/></svg>
          <span>elias@tarvimoor.com</span>
        </li>
        <li class="contact__item">
          <svg viewBox="0 0 14 14"><circle cx="7" cy="7" r="6.5"/></svg>
          <span>www.tarvimoor.com</span>
        </li>
      </ul>
    </div>
  </section>
</main>
</body>
</html>
```